PLUM TRACKER

WEBSITE AND HTML FOR A WEBSITE LOGO AND CONTENT ATTACHED HERES A COMPETITORS
https://www.lintorbay.com/

Coded - Design and coding required

1 page

```html
<!DOCTYPE html>
<html lang="en">
<head>
<meta charset="utf-8">
<title>Plum Tracker – Creator Management Agency</title>
<link href="https://fonts.googleapis.com/css2?family=Fira+Sans:wght@500;600;700&family=Jost:wght@400;500;600&display=swap" rel="stylesheet">
<style>
:root{
  --teal:#2a7a7d;
  --teal-dark:#1f5f62;
  --pink:#e08fb0;
  --pink-soft:#eaa4c0;
  --blush:#f9ece6;
  --aqua:#d6eff1;
  --aqua-light:#e6f5f6;
  --ink:#1e1e1e;
  --line:#a9d1d3;
  --white:#ffffff;
}
*{margin:0;padding:0;box-sizing:border-box}
html,body{width:1200px;height:3606px;overflow:hidden}
body{position:relative;font-family:"Jost",sans-serif;color:var(--ink);background:var(--white)}
.abs{position:absolute}
.heading{font-family:"Fira Sans",sans-serif;font-weight:600}
.dot::after{content:"";display:inline-block;width:.22em;height:.22em;border-radius:50%;background:var(--pink);margin-left:.08em}
.art{position:absolute;border-radius:24px}

/* header */
.site-header{top:0;left:0;width:1200px;height:93px;background:var(--white)}
.brand{left:92px;top:28px;font-family:"Fira Sans",sans-serif;font-weight:600;font-size:31px;color:var(--teal);display:flex;align-items:center;gap:10px;letter-spacing:.5px}
.brand-mark{width:14px;height:14px;border-radius:50%;background:var(--pink)}
.main-nav a,.footer-nav a{position:absolute;text-decoration:none;font-weight:500;letter-spacing:.5px}
.main-nav a{top:38px;font-size:13.5px;color:var(--teal-dark)}
.main-nav a.active::after{content:"";position:absolute;left:0;right:0;bottom:-10px;height:2px;background:var(--pink)}
.cta{left:933px;top:24px;width:190px;height:44px;border-radius:4px;background:#cdeced;color:var(--teal);font-size:13px;font-weight:500;display:flex;align-items:center;justify-content:center;letter-spacing:.5px}

/* hero */
.hero{top:93px;left:0;width:1200px;height:631px;background:var(--blush);overflow:hidden}
.hero-circle{left:-130px;top:-70px;width:222px;height:222px;border-radius:50%;background:var(--pink)}
.hero-title{left:110px;top:150px;width:470px;font-size:27px;line-height:38.5px;color:var(--teal)}
.hero-text{left:113px;top:325px;width:400px;font-size:18.5px;line-height:30px}
.scroll-btn{left:583px;top:691px;width:66px;height:66px;border-radius:50%;background:var(--white);border:1.5px solid var(--line);display:flex;align-items:center;justify-content:center}

/* features */
.feature{position:absolute;top:1045px;width:300px;text-align:center}
.feature h3{font-size:23px;margin-bottom:12px}
.feature p{font-size:14px;line-height:22px;width:258px;margin:0 auto}

/* services */
.services{top:1355px;left:0;width:1200px;height:730px;background:var(--aqua)}
.section-title{font-size:42px;color:var(--teal)}
.services-title{top:1420px;left:0;width:1200px;text-align:center}
.divider{left:609px;top:1545px;width:1px;height:435px;background:#b9dcdf}
.service{position:absolute;top:1815px;width:470px;text-align:center}
.service h3{font-size:30px;margin-bottom:8px}
.service p{font-size:16px;line-height:23.5px;width:450px;margin:0 auto}
.pink-num{color:var(--pink)}

/* faq */
.faq{top:2085px;left:0;width:1200px;height:747px;background:var(--blush)}
.faq-title{left:574px;top:2190px}
.faq-item{position:absolute;left:574px;width:531px;border-bottom:1.5px solid var(--line)}
.faq-item.last{border-bottom:none}
.faq-q{font-family:"Fira Sans",sans-serif;font-weight:500;font-size:17px;line-height:21px;color:#2b2b2b;width:460px}
.faq-a{font-size:16px;line-height:23.5px;margin-top:12px;width:490px}
.chev{position:absolute;right:8px;top:6px}

/* contact */
.contact{top:2832px;left:0;width:1200px;height:628px;background:linear-gradient(180deg,var(--aqua),var(--aqua-light));overflow:hidden}
.contact-circle{left:-175px;top:-215px;width:350px;height:350px;border-radius:50%;background:var(--pink)}
.contact-title{left:110px;top:2960px}
.contact-sub{left:115px;top:3030px;width:400px;font-family:"Fira Sans",sans-serif;font-weight:500;font-size:19px;line-height:30px;color:#2b2b2b}
.contact-fill{left:115px;top:3120px;font-size:16px}
.contact-email{left:115px;top:3150px;font-size:17px;color:var(--teal);font-weight:600;text-decoration:underline}
.form-card{left:557px;top:2888px;width:516px;height:497px;border-radius:14px;background:rgba(255,255,255,.6)}
.label{position:absolute;font-family:"Fira Sans",sans-serif;font-size:11.5px;font-weight:600;color:var(--teal)}
.field{position:absolute;height:37px;border:1px solid var(--line);border-radius:3px;background:var(--white);font-size:10px;color:#888;padding:0 14px;display:flex;align-items:center}
.send{left:609px;top:3320px;width:117px;height:36px;border-radius:3px;background:var(--pink-soft);color:var(--white);font-family:"Fira Sans",sans-serif;font-weight:600;font-size:15px;display:flex;align-items:center;justify-content:center;gap:6px}

/* footer */
.footer-nav a{top:3496px;font-size:15px;color:#2b2b2b}
.copyright{top:3538px;left:0;width:1200px;text-align:center;font-size:13px;color:#6a8f91}
</style>
</head>
<body>

<header class="abs site-header">
  <div class="abs brand"><span class="brand-mark"></span>PLUM TRACKER</div>
  <nav class="main-nav">
    <a href="#" class="active" style="left:448px">HOME</a>
    <a href="#" style="left:532px">TOGETHER</a>
    <a href="#" style="left:651px">SERVICES</a>
    <a href="#" style="left:760px">ABOUT</a>
    <a href="#" style="left:856px">FAQ</a>
  </nav>
  <a class="abs cta">FREE CONSULTATION</a>
</header>

<section class="abs hero">
  <div class="abs hero-circle"></div>
  <h1 class="abs heading hero-title">Plum Tracker is a full-service FanVault management agency that specialises in chat management, promotion and traffic analysis.</h1>
  <p class="abs hero-text">Our strategies have helped creators reach the top 1% of FanVault. Our nothing to pay upfront approach makes it accessible for both smaller and bigger creators.</p>
  <div class="art" role="img" aria-label="Line illustration of a woman working on a laptop with a paper plane flying" style="left:548px;top:80px;width:602px;height:420px;background:linear-gradient(135deg,rgba(42,122,125,.18),rgba(224,143,176,.22))"></div>
</section>
<div class="abs scroll-btn">
  <svg width="24" height="28" viewBox="0 0 24 28" fill="none" stroke="#2a7a7d" stroke-width="1.6"><path d="M12 2v23M3 16l9 9 9-9"/></svg>
</div>

<div class="art" role="img" aria-label="Line drawing of a hand holding up a key" style="left:195px;top:780px;width:150px;height:255px;background:linear-gradient(180deg,rgba(42,122,125,.15),rgba(224,143,176,.15))"></div>
<div class="art" role="img" aria-label="Line drawing of two joined puzzle pieces" style="left:510px;top:820px;width:205px;height:195px;background:linear-gradient(135deg,rgba(42,122,125,.15),rgba(224,143,176,.2))"></div>
<div class="art" role="img" aria-label="Line drawing of hands holding a growing plant" style="left:835px;top:800px;width:235px;height:215px;background:linear-gradient(180deg,rgba(224,143,176,.18),rgba(42,122,125,.15))"></div>

<div class="feature" style="left:108px">
  <h3 class="heading dot">Power to creators</h3>
  <p>We take care of your FanVault account, so you can focus on creating content for your fans. Plum Tracker makes your experience as a content creator simple and stress free.</p>
</div>
<div class="feature" style="left:460px">
  <h3 class="heading dot">Building together</h3>
  <p>Connecting to our creators on a personal level is essential to us. We need to know you in order to understand what is best for you. We work together as a team.</p>
</div>
<div class="feature" style="left:802px">
  <h3 class="heading dot">Personalised growth</h3>
  <p>Every creator is unique and requires a distinct approach. Using powerful analytic tools we are able to optimise your social media outlets and reach millions of potential clients.</p>
</div>

<section class="abs services"></section>
<h2 class="abs heading section-title services-title dot">Services</h2>
<div class="abs divider"></div>
<div class="art" role="img" aria-label="Line drawing of a laptop with chat bubbles" style="left:185px;top:1550px;width:280px;height:200px;background:linear-gradient(135deg,rgba(255,255,255,.55),rgba(224,143,176,.2))"></div>
<div class="art" role="img" aria-label="Line drawing of a hand holding a megaphone" style="left:695px;top:1550px;width:300px;height:230px;background:linear-gradient(135deg,rgba(224,143,176,.2),rgba(42,122,125,.2))"></div>
<div class="service" style="left:97px">
  <h3 class="heading">Earning 24/<span class="pink-num dot">7</span></h3>
  <p>Our trained team manages your chat 7 days a week to retain and gain more subscribers. The constant stream of messages can become hard to keep up with for creators. We take care of your chats and have shown to increase income from messages by up to a <b>100 times.</b></p>
</div>
<div class="service" style="left:638px">
  <h3 class="heading dot">Viral strategies</h3>
  <p>We offer a personalised growth plan to every creator in order to maximise your reach. Our strategies have made creators go viral and amass millions of views on ClipStream. Our creators have gained <b>thousands</b> of paid fans from viral ClipStream video's.</p>
</div>

<section class="abs faq"></section>
<div class="art" role="img" aria-label="Line drawing of an open hand holding a large question mark" style="left:0;top:2225px;width:505px;height:475px;border-radius:0 24px 24px 0;background:linear-gradient(135deg,rgba(42,122,125,.2),rgba(224,143,176,.2))"></div>
<h2 class="abs heading section-title faq-title dot">FAQ</h2>
<div class="faq-item" style="top:2278px;height:45px">
  <p class="faq-q">When can I get started?</p>
  <svg class="chev" width="14" height="9" viewBox="0 0 14 9" fill="none" stroke="#2a7a7d" stroke-width="1.6"><path d="M1 1l6 6 6-6"/></svg>
</div>
<div class="faq-item" style="top:2347px;height:128px">
  <p class="faq-q">What do your services include?</p>
  <p class="faq-a">Chat management, copywriting, content scheduling, viral social media strategies, content plans and more! Our services are tailored specifically for you.</p>
  <svg class="chev" width="14" height="9" viewBox="0 0 14 9" fill="none" stroke="#2a7a7d" stroke-width="1.6"><path d="M1 8l6-6 6 6"/></svg>
</div>
<div class="faq-item" style="top:2507px;height:78px">
  <p class="faq-q">I don't have an FanVault account or I have a very small subscriber base, is this service right for me?</p>
  <svg class="chev" width="14" height="9" viewBox="0 0 14 9" fill="none" stroke="#2a7a7d" stroke-width="1.6"><path d="M1 1l6 6 6-6"/></svg>
</div>
<div class="faq-item last" style="top:2625px;height:50px">
  <p class="faq-q">I already have a large following, but I cannot manage it on my own anymore, is this service right for me?</p>
  <svg class="chev" width="14" height="9" viewBox="0 0 14 9" fill="none" stroke="#2a7a7d" stroke-width="1.6"><path d="M1 1l6 6 6-6"/></svg>
</div>

<section class="abs contact">
  <div class="abs contact-circle"></div>
  <div class="art" role="img" aria-label="Paper plane with dashed flight trail" style="left:0;top:385px;width:470px;height:130px;border-radius:0 24px 24px 0;background:linear-gradient(90deg,rgba(42,122,125,.06),rgba(42,122,125,.12))"></div>
</section>
<h2 class="abs heading section-title contact-title dot">Get in touch</h2>
<p class="abs contact-sub">Want to become a top earner or need help managing a large subscriber base?</p>
<p class="abs contact-fill">Fill Our form or contat us on below email:</p>
<a class="abs contact-email">hello@plumtracker.com</a>

<form class="abs form-card"></form>
<span class="label" style="left:598px;top:2930px">Name*</span>
<div class="field" style="left:598px;top:2953px;width:202px">First Name</div>
<div class="field" style="left:809px;top:2953px;width:203px">Last Name</div>
<span class="label" style="left:601px;top:3003px">Email*</span>
<div class="field" style="left:601px;top:3026px;width:409px">Email address</div>
<span class="label" style="left:601px;top:3076px">ChatLine</span>
<div class="field" style="left:602px;top:3099px;width:410px"></div>
<span class="label" style="left:603px;top:3149px">ClipStream</span>
<div class="field" style="left:603px;top:3172px;width:410px"></div>
<span class="label" style="left:607px;top:3221px">Message *</span>
<div class="field" style="left:607px;top:3244px;width:409px;height:64px"></div>
<div class="abs send">Send
  <svg width="13" height="13" viewBox="0 0 14 14" fill="#fff"><path d="M13 1L1 6l4 2 6-5-5 6v4l2-3 3 2z"/></svg>
</div>

<nav class="footer-nav">
  <a href="#" style="left:232px">HOME</a>
  <a href="#" style="left:327px">TOGETHER</a>
  <a href="#" style="left:458px">SERVICES</a>
  <a href="#" style="left:581px">ABOUT</a>
  <a href="#" style="left:687px">FAQ</a>
  <a href="#" style="left:769px">FREE CONSULTATION</a>
</nav>
<p class="abs copyright">© Copyright 2022 Plum Tracker All Right Reserved</p>

</body>
</html>
```